Business cards and logo for Pellicott Law, P.A.

I need a business card and logo design for a new law firm in Miami, Florida called Pellicott Law, P.A. I, Dominic R. Pellicott, am the only lawyer in the firm. The law firm will mainly serve businesses but will also handle many other cases. Preferred colors are green and/or gray, but open minded to other suggestions.

Industry/Entity Type

Legal

Contact Information for Business Card

Phone Number TBD. Address is:
412 NE 19TH AVE STE 230
MIAMI, FL 33152

```html
<!DOCTYPE html>
<html lang="en">
<head>
<meta charset="utf-8">
<title>Pellicott Law, P.A. — Business Card</title>
<link rel="stylesheet" href="https://fonts.googleapis.com/css2?family=Tinos:wght@400;700&display=swap">
<style>
  :root {
    --navy: #14466a;
    --gray: #a6a6a6;
    --icon-gray: #a3a9ae;
    --white: #ffffff;
    --backdrop: #e6e3de;
  }
  * { box-sizing: border-box; margin: 0; padding: 0; }
  html, body {
    width: 1200px;
    height: 902px;
    overflow: hidden;
    background: var(--backdrop);
  }
  .card {
    position: absolute;
    left: 80px;
    top: 154px;
    width: 1040px;
    height: 592px;
    background: var(--white);
    border-radius: 24px;
    overflow: hidden;
    box-shadow: 0 8px 28px rgba(0,0,0,0.12);
    font-family: "Tinos", "Times New Roman", serif;
  }
  .card__bands {
    position: absolute;
    inset: 0;
    width: 100%;
    height: 100%;
  }
  .brand {
    position: absolute;
    left: 47px;
    width: 400px;
    text-align: center;
    color: var(--navy);
  }
  .brand__mark {
    position: absolute;
    left: 212px;
    top: 86px;
    width: 70px;
    height: 70px;
    background: var(--navy);
  }
  .brand__name {
    top: 250px;
    font-weight: 700;
    font-size: 33px;
    line-height: 1;
    letter-spacing: 0.3px;
  }
  .brand__owner {
    top: 292px;
    font-weight: 700;
    font-size: 26px;
    line-height: 1;
  }
  .holder {
    position: absolute;
    right: 42px;
    text-align: right;
    line-height: 1;
  }
  .holder__name {
    top: 72px;
    font-size: 32px;
    color: var(--navy);
    letter-spacing: 0.5px;
  }
  .holder__title {
    top: 110px;
    font-size: 25px;
    color: var(--gray);
  }
  .contact {
    position: absolute;
    right: 42px;
    color: var(--white);
    font-size: 26px;
    line-height: 1;
    text-align: right;
  }
  .contact--street { top: 377px; }
  .contact--city { top: 410px; }
  .contact-line {
    position: absolute;
    right: 43px;
    display: flex;
    align-items: center;
    gap: 12px;
    color: var(--white);
    font-size: 26px;
    line-height: 1;
  }
  .contact-line--phone { top: 464px; }
  .contact-line--email { top: 500px; }
  .contact-line__icon {
    width: 28px;
    height: 28px;
    display: block;
  }
</style>
</head>
<body>
  <main class="card">
    <svg class="card__bands" viewBox="0 0 1040 592" aria-hidden="true">
      <polygon fill="var(--gray)" points="548,335 566,335 386,592 368,592"/>
      <polygon fill="var(--navy)" points="590,335 1040,335 1040,592 410,592"/>
      <rect fill="var(--navy)" x="0" y="556" width="1040" height="36"/>
      <rect fill="var(--gray)" x="0" y="544" width="376" height="6"/>
    </svg>

    <div class="brand__mark" aria-hidden="true"></div>
    <p class="brand brand__name">PELLICOTT LAW, P.A.</p>
    <p class="brand brand__owner">Dominic R. Pellicott</p>

    <p class="holder holder__name">DOMINIC R. PELLICOTT</p>
    <p class="holder holder__title">President</p>

    <p class="contact contact--street">412 NE 19TH AVE STE 230</p>
    <p class="contact contact--city">MIAMI, FL 33152</p>

    <p class="contact-line contact-line--phone">
      <span>+01-555-210-4830</span>
      <svg class="contact-line__icon" viewBox="0 0 29 29" aria-label="Phone">
        <rect width="29" height="29" rx="4" fill="var(--icon-gray)"/>
        <path fill="var(--navy)" d="M10.5,6.5 l3,0.6 l0.8,4.2 l-2.2,1.4 c0.6,2.2 1.6,3.6 3,5 l2.1,-1.3 l3.4,2.6 l-1.2,2.8 c-5.8,-0.5 -10.2,-7.6 -8.9,-15.3 Z"/>
      </svg>
    </p>
    <p class="contact-line contact-line--email">
      <span>Info@pellicottlawfirm.com</span>
      <svg class="contact-line__icon" viewBox="0 0 29 29" aria-label="Email">
        <rect width="29" height="29" rx="4" fill="var(--icon-gray)"/>
        <rect x="6" y="9" width="17" height="12" fill="var(--white)"/>
        <path d="M6,9 L14.5,16 L23,9" fill="none" stroke="var(--icon-gray)" stroke-width="1.5"/>
      </svg>
    </p>
  </main>
</body>
</html>
```